Non Profit Company Looking For New Website

The website for Corvale Paddock Rehoming Society should offer the viewer beautiful photos that inspire condifence and joy and tap into our love of horses.

We would like to see a website that displays trust, quality and confidence. Needs to be responsive and mobile friendly for all browsers and coded for both Android & IOS.

READ ATTACHED WEBSITE TEMPLATE FOR COMPLETE DETAILS ON WHAT WE ARE LOOKING FOR.

Looking for recommmendations if we should use WordPress/WooCommerce for site or Wordpress with Shopify Plug in or just Shopify.

Must be both desktop and mobile friendly with fast page load speed. Need the ability to edit ourselves.

Industry/Entity Type

Non Profit

Coding

Coded - Design and coding required

Number of Pages Required

5+ page

Requirements
Must have
• We would like to see a website that displays trust, quality and confidence. Needs to be responsive and mobile friendly for all browsers and coded for both Android & IOS.

Looking for recommendations if we should use WordPress/WooCommerce for site or Wordpress with Shopify Plug in or just Shopify.

Logo Colour:
Pantone 7621 C

READ TEMPLATE THAT IS ATTACHED
Nice to have
• Like look of this website as a sample:
https://www.quillmanegallop.com/

Another similar non profit organization
https://brindlefieldrest.com/

```html
<!DOCTYPE html>
<html lang="en">
<head>
<meta charset="utf-8">
<title>Corvale Paddock Rehoming Society</title>
<link href="https://fonts.googleapis.com/css2?family=Raleway:wght@400;500;600;700&family=Open+Sans:wght@400;600;700&display=swap" rel="stylesheet">
<style>
:root{
  --red:#b1232a;
  --red-dark:#8e1a20;
  --ink:#1f1f1f;
  --muted:#8a8a8a;
  --white:#ffffff;
  --footer:#f1f1f1;
  --line:#c9c9c9;
}
*{box-sizing:border-box;margin:0;padding:0}
html,body{width:1200px;height:4100px;overflow:hidden}
body{font-family:"Open Sans",sans-serif;color:var(--ink);background:var(--white);position:relative}
.abs{position:absolute}
.btn{display:flex;align-items:center;justify-content:center;font-family:"Open Sans",sans-serif;font-weight:700;letter-spacing:1px;font-size:15px;text-transform:uppercase}
.photo{position:absolute}

/* header / hero */
.hero{position:absolute;left:0;top:0;width:1200px;height:720px;background:linear-gradient(120deg,#5b3a24 0%,#8a5a3a 30%,#4a2e1e 60%,#7a4c30 100%)}
.hero-shade{position:absolute;inset:0;background:rgba(20,10,6,.42)}
.nav{position:absolute;top:14px;display:flex;gap:34px;font-size:14px;font-weight:600;color:var(--white);letter-spacing:.5px}
.nav-left{left:214px}
.nav-right{left:724px;align-items:center}
.logo-box{position:absolute;left:520px;top:0;width:160px;height:128px;background:var(--white);display:flex;flex-direction:column;align-items:center;justify-content:center;text-align:center;color:var(--red);font-family:"Raleway",sans-serif;font-weight:700;box-shadow:0 4px 14px rgba(0,0,0,.2)}
.logo-box .big{font-size:26px;line-height:1}
.logo-box .small{font-size:10px;line-height:1.3;margin-top:8px;letter-spacing:.5px;text-transform:uppercase}
.hero-title{position:absolute;left:160px;top:258px;width:880px;text-align:center;font-family:"Raleway",sans-serif;font-weight:400;font-size:40px;line-height:1.3;color:var(--white)}
.hero-title b{font-weight:700}
.hero-btn{position:absolute;left:450px;top:500px;width:300px;height:72px;background:var(--white);color:var(--red)}

/* paths */
.paths{position:absolute;left:248px;top:800px;display:flex;gap:16px}
.path-card{position:relative;width:224px;height:232px;overflow:hidden;box-shadow:0 3px 10px rgba(0,0,0,.2)}
.path-card .photo{inset:0}
.path-card .tint{position:absolute;inset:0;background:linear-gradient(to bottom,rgba(177,35,42,0) 40%,rgba(177,35,42,.85) 100%)}
.path-card span{position:absolute;left:20px;bottom:16px;font-family:"Raleway",sans-serif;font-weight:700;font-size:32px;color:var(--white)}
.intro{position:absolute;left:300px;top:1076px;width:600px;text-align:center;font-size:15px;line-height:1.6}

/* what is */
.what-photo{left:0;top:1200px;width:600px;height:532px;background:linear-gradient(135deg,#3a2a22 0%,#6b4a3a 45%,#b08a70 70%,#2b201b 100%)}
.what-panel{position:absolute;left:600px;top:1200px;width:600px;height:532px;background:var(--red);color:var(--white)}
.what-panel h2{position:absolute;left:64px;top:44px;font-family:"Raleway",sans-serif;font-weight:500;font-size:52px;line-height:1.1}
.what-panel h2 b{font-weight:700}
.what-panel p{position:absolute;left:64px;width:400px;font-size:12px;line-height:1.55}
.what-btn{position:absolute;left:64px;top:412px;width:280px;height:48px;border:2px solid var(--white);color:var(--white);font-size:13px}

/* adopt */
.adopt-title{position:absolute;left:140px;top:1850px;font-family:"Raleway",sans-serif;font-weight:500;font-size:52px}
.adopt-title b{color:var(--red);font-weight:600}
.adopt-text{position:absolute;left:140px;top:1930px;width:340px;font-size:12px;line-height:1.55;color:#444}
.adopt-btn{position:absolute;left:140px;top:2020px;width:204px;height:46px;background:var(--red);color:var(--white);font-size:13px}
.adopt-photo{left:600px;top:1732px;width:600px;height:480px;background:linear-gradient(160deg,#cfd46a 0%,#8fa83a 40%,#4f6a2a 75%,#2d3a18 100%)}

/* featured */
.featured{position:absolute;left:0;top:2212px;width:1200px;height:760px;background:var(--red)}
.arrow{position:absolute;top:2256px}
.feature-card{position:absolute;left:152px;top:2300px;width:440px;height:352px;background:linear-gradient(140deg,#2a1612 0%,#5a3424 60%,#1c0f0c 100%)}
.feature-card .shade{position:absolute;inset:0;background:rgba(0,0,0,.3)}
.feature-card h3{position:absolute;left:36px;top:36px;font-family:"Raleway",sans-serif;font-weight:700;font-size:40px;color:var(--white)}
.feature-card p{position:absolute;left:36px;top:96px;width:320px;font-size:12px;line-height:1.5;color:#eee}
.feature-card .stats{position:absolute;left:36px;top:152px;display:flex;gap:18px;font-size:13px;color:var(--white)}
.feature-card .stats b{font-weight:700}
.feature-btn{position:absolute;left:36px;top:204px;width:200px;height:44px;background:var(--white);color:var(--red);font-size:13px}
.feature-photo{left:612px;top:2300px;width:436px;height:352px;background:linear-gradient(135deg,#c9d8e8 0%,#a35a2a 45%,#7a3a18 70%,#d9c9b0 100%)}
.thumbs{position:absolute;left:152px;top:2672px;display:flex;gap:16px}
.thumb{width:212px;height:140px}
.give-btn{position:absolute;left:468px;top:2864px;width:264px;height:56px;border:2px solid var(--white);color:var(--white);font-size:13px}

/* contact */
.contact-title{position:absolute;left:140px;top:3076px;font-family:"Raleway",sans-serif;font-weight:500;font-size:52px;line-height:1.15}
.contact-title .accent{color:var(--red)}
.field{position:absolute;border-bottom:2px solid var(--line);height:40px;font-size:13px;color:var(--muted);padding-top:6px}
.submit{position:absolute;left:140px;top:3496px;width:232px;height:50px;background:var(--red);color:var(--white);font-size:14px}
.contact-card{position:absolute;left:764px;top:3088px;width:292px;height:472px;background:var(--red);color:var(--white);border-radius:6px;overflow:hidden}
.contact-card h4{position:absolute;left:36px;top:32px;font-family:"Raleway",sans-serif;font-weight:700;font-size:28px}
.c-row{position:absolute;left:36px;display:flex;align-items:center;gap:14px;font-size:12px;line-height:1.35;width:230px}
.c-icon{flex:0 0 30px;height:30px;background:var(--white);border-radius:4px;display:flex;align-items:center;justify-content:center}
.contact-photo{left:0;bottom:0;width:292px;height:160px;background:linear-gradient(to top,#5a1016 0%,#8e1a20 40%,rgba(142,26,32,0) 100%)}

/* footer */
.footer{position:absolute;left:0;top:3680px;width:1200px;height:420px;background:var(--footer)}
.foot-logo{position:absolute;left:152px;top:3752px;width:160px;height:160px;background:var(--white);display:flex;flex-direction:column;align-items:center;justify-content:center;text-align:center;color:var(--red);font-family:"Raleway",sans-serif;font-weight:700;box-shadow:0 2px 8px rgba(0,0,0,.12)}
.foot-logo .big{font-size:28px;line-height:1}
.foot-logo .small{font-size:10px;line-height:1.3;margin-top:8px;text-transform:uppercase}
.foot-photo{left:192px;top:3800px;width:310px;height:300px;background:linear-gradient(160deg,#d9a27a 0%,#a4582c 45%,#6a3416 100%)}
.foot-col{position:absolute;top:3766px;display:flex;flex-direction:column;gap:12px;font-size:13px;color:var(--red);font-weight:600}
.foot-rule{position:absolute;left:588px;top:3950px;width:460px;height:2px;background:var(--red)}
.socials{position:absolute;left:588px;top:3976px;display:flex;gap:10px}
.social{width:24px;height:24px;background:var(--red);border-radius:3px}
.copy{position:absolute;left:880px;top:3980px;font-size:11px;color:var(--muted)}
.legal{position:absolute;left:588px;top:4060px;width:612px;height:40px;background:var(--red);display:flex;gap:60px;align-items:center;padding-left:160px;color:var(--white);font-size:12px}
</style>
</head>
<body>

<section class="hero">
  <div class="photo" role="img" aria-label="Photo of several chestnut thoroughbred horses standing together" style="inset:0;background:linear-gradient(120deg,#5b3a24 0%,#8a5a3a 30%,#4a2e1e 60%,#7a4c30 100%)"></div>
  <div class="hero-shade"></div>
  <nav class="nav nav-left"><span>HOME</span><span>ABOUT</span><span>ADOPT</span><span>HORSES</span></nav>
  <nav class="nav nav-right"><span>SHOP</span><span>DONATION</span><span>CONTACT US</span>
    <svg width="22" height="20" viewBox="0 0 22 20" aria-label="Cart"><path d="M1 2h4l3 11h10l3-8H6" fill="none" stroke="#fff" stroke-width="2"/><circle cx="9" cy="17" r="2" fill="#fff"/><circle cx="17" cy="17" r="2" fill="#fff"/></svg>
  </nav>
  <div class="logo-box"><span class="big">Corvale</span><span class="small">Paddock Rehoming<br>Society</span></div>
  <h1 class="hero-title">We <b>support and develop retired thoroughbred racehorses</b> for their next chapter in life</h1>
  <a class="btn hero-btn">See our horses</a>
</section>

<div class="paths">
  <div class="path-card"><div class="photo" role="img" aria-label="Photo of a retired racehorse" style="background:linear-gradient(150deg,#6a3a26,#3a1f14)"></div><div class="tint"></div><span>Retire</span></div>
  <div class="path-card"><div class="photo" role="img" aria-label="Photo of a rider retraining a horse" style="background:linear-gradient(150deg,#7a8fb0,#4a3a30)"></div><div class="tint"></div><span>Retrain</span></div>
  <div class="path-card"><div class="photo" role="img" aria-label="Photo of a horse in its new home" style="background:linear-gradient(150deg,#8a4a2a,#2e1a12)"></div><div class="tint"></div><span>Rehome</span></div>
</div>
<p class="intro"><b>Corvale Paddock Rehoming Society (CPRS)</b> is a registered<br>not-for-profit organization in Alberta.</p>

<div class="photo what-photo" role="img" aria-label="Photo of a person gently resting a hand on a horse's head"></div>
<section class="what-panel">
  <h2>What is<br><b>Thoroughbred<br>Aftercare?</b></h2>
  <p style="top:212px">The health, safety and welfare of our horses after racing matter to us every day. Owners, trainers and volunteers work together to give each horse the care it deserves.</p>
  <p style="top:282px">Aftercare is the safe placement of racehorses once their careers are finished. Some horses retire to pasture, while others are retrained for a new sport or a quiet life.</p>
  <a class="btn what-btn">Learn more about us</a>
</section>

<h2 class="adopt-title">Adopt a <b>Horse</b></h2>
<p class="adopt-text">Corvale Paddock Rehoming Society is committed to helping match you with the perfect horse.</p>
<a class="btn adopt-btn">Adopt now</a>
<div class="photo adopt-photo" role="img" aria-label="Photo of a young girl lying across the back of a pinto horse in a green field"></div>

<section class="featured"></section>
<svg class="arrow" style="left:70px;top:2460px" width="20" height="36" viewBox="0 0 20 36" aria-label="Previous"><path d="M17 2L3 18l14 16" fill="none" stroke="#fff" stroke-width="3" opacity=".7"/></svg>
<svg class="arrow" style="left:1110px;top:2460px" width="20" height="36" viewBox="0 0 20 36" aria-label="Next"><path d="M3 2l14 16L3 34" fill="none" stroke="#fff" stroke-width="3" opacity=".7"/></svg>
<div class="feature-card" role="img" aria-label="Photo of the featured horse Open Sesame">
  <div class="shade"></div>
  <h3>Open Sesame</h3>
  <p>A gentle, willing gelding with a calm temper who loves people and is ready for a new career with a patient rider.</p>
  <div class="stats"><span>Year: <b>2013</b></span><span>Height: <b>16.2</b></span><span>Born: <b>2013</b></span></div>
  <a class="btn feature-btn">View horse</a>
</div>
<div class="photo feature-photo" role="img" aria-label="Photo of a chestnut horse with a white blaze"></div>
<div class="thumbs">
  <div class="thumb" role="img" aria-label="Photo of a bay horse" style="background:linear-gradient(150deg,#7a8a5a,#3a2618)"></div>
  <div class="thumb" role="img" aria-label="Photo of a dark horse" style="background:linear-gradient(150deg,#b7c8d8,#2a1a12)"></div>
  <div class="thumb" role="img" aria-label="Photo of a chestnut horse" style="background:linear-gradient(150deg,#c8d8e6,#9a4a22)"></div>
  <div class="thumb" role="img" aria-label="Photo of a grey horse" style="background:linear-gradient(150deg,#6a5a4a,#d8d0c4)"></div>
</div>
<a class="btn give-btn">More ways to give</a>

<h2 class="contact-title">Have a question or<br><span class="accent">Need more information?</span></h2>
<div class="field" style="left:140px;top:3236px;width:260px">First name</div>
<div class="field" style="left:452px;top:3236px;width:248px">Last name</div>
<div class="field" style="left:140px;top:3316px;width:260px">Contact number</div>
<div class="field" style="left:452px;top:3316px;width:248px">Email address</div>
<div class="field" style="left:140px;top:3396px;width:560px">Your message</div>
<a class="btn submit">Submit</a>

<aside class="contact-card">
  <h4>Contact Us</h4>
  <div class="c-row" style="top:96px"><span class="c-icon"><svg width="16" height="16" viewBox="0 0 16 16"><path d="M3 1l3 3-2 2c1 2 3 4 5 5l2-2 3 3-2 3C7 15 1 9 1 3z" fill="#b1232a"/></svg></span>+1 (587) 555-0142</div>
  <div class="c-row" style="top:150px"><span class="c-icon"><svg width="16" height="12" viewBox="0 0 16 12"><rect x="1" y="1" width="14" height="10" fill="none" stroke="#b1232a" stroke-width="1.6"/><path d="M1 1l7 6 7-6" fill="none" stroke="#b1232a" stroke-width="1.6"/></svg></span>hello@corvalepaddock.org</div>
  <div class="c-row" style="top:204px"><span class="c-icon"><svg width="12" height="16" viewBox="0 0 12 16"><path d="M6 15S1 9 1 6a5 5 0 0110 0c0 3-5 9-5 9z" fill="#b1232a"/><circle cx="6" cy="6" r="2" fill="#fff"/></svg></span>218 Meadowlark Lane,<br>Red Deer AB T4N 0X2</div>
  <div class="photo contact-photo" role="img" aria-label="Photo of a grey horse cantering along a fence line"></div>
</aside>

<footer class="footer"></footer>
<div class="photo foot-photo" role="img" aria-label="Photo of a chestnut horse head and neck"></div>
<div class="foot-logo"><span class="big">Corvale</span><span class="small">Paddock Rehoming<br>Society</span></div>
<div class="foot-col" style="left:588px"><span>HOME</span><span>ABOUT</span><span>ADOPT</span><span>HORSES</span></div>
<div class="foot-col" style="left:720px"><span>SHOP</span><span>DONATION</span><span>CONTACT US</span></div>
<div class="foot-col" style="left:900px"><span>HELLO@CORVALEPADDOCK.ORG</span><span>+1 (587) 555-0142</span><span>218 MEADOWLARK LANE,<br>RED DEER AB T4N 0X2</span></div>
<div class="foot-rule"></div>
<div class="socials"><span class="social"></span><span class="social"></span><span class="social"></span><span class="social"></span><span class="social"></span></div>
<div class="copy">Copyright © 2024 Corvale Paddock</div>
<div class="legal"><span>Terms &amp; conditions</span><span>Privacy policy</span></div>

</body>
</html>
```